Building business client journey document

We want to design a journey document which helps our clients understand the process of building a house from initial conversations through to construction. I have attached an example along with the design of stages/writing we would like for ours.

```html
<!DOCTYPE html>
<html lang="en">
<head>
<meta charset="utf-8">
<title>Client Journey – Building Your Home</title>
<link href="https://fonts.googleapis.com/css2?family=Oswald:wght@500;600&family=Open+Sans:wght@400&display=swap" rel="stylesheet">
<style>
:root{
  --green:#22a24b;
  --green-light:#3cc064;
  --green-border:#2fb065;
  --green-deep:#0f6b35;
  --green-mid:#17803f;
  --band:#2a2a2a;
  --page:#f1f2f2;
  --ink:#333;
  --icon:#2b2b2b;
  --sky:#bfe5ee;
}
*{box-sizing:border-box;margin:0;padding:0}
html,body{width:713px;height:1200px;overflow:hidden;background:var(--page)}
.journey{position:relative;width:713px;height:1200px;background:var(--page);font-family:"Open Sans",Arial,sans-serif;color:var(--ink)}
.top-bar{position:absolute;left:0;top:0;width:713px;height:58px;background:linear-gradient(180deg,var(--green-light),var(--green))}
.stage-band{position:absolute;height:24px;background:var(--band);color:#fff;font-family:"Oswald",Arial,sans-serif;font-weight:500;font-size:13px;line-height:24px;clip-path:polygon(0 0,calc(100% - 12px) 0,100% 50%,calc(100% - 12px) 100%,0 100%)}
.stage-band .stage-no{position:absolute;left:16px}
.stage-band .stage-name{position:absolute;left:0;right:0;text-align:center}
.step-icon{position:absolute;width:70px;height:64px}
.step-card{position:absolute;width:178px;background:#fff;border:2px solid var(--green-border);border-radius:8px;padding:6px 14px}
.step-card h3{font-family:"Oswald",Arial,sans-serif;font-weight:500;font-size:10.5px;color:var(--green);text-align:center;text-transform:uppercase;margin-bottom:6px;line-height:1.2}
.step-card p{font-size:8.6px;line-height:12px}
.connector{position:absolute;width:40px;height:18px;background:var(--icon)}
.connector.right{clip-path:polygon(0 0,80% 0,100% 50%,80% 100%,0 100%,12% 50%)}
.connector.left{clip-path:polygon(20% 0,100% 0,88% 50%,100% 100%,20% 100%,0 50%)}
.variation-note{position:absolute;left:420px;top:695px;width:100px;font-size:8.6px;line-height:12px;text-align:center}
.variation-line{position:absolute;left:463px;top:737px;width:9px;height:190px;background:repeating-linear-gradient(45deg,#555 0 1.5px,#fff 1.5px 4px)}
.icon-placeholder{background:#3a3a3a;border-radius:6px;opacity:.85}
.track{position:absolute;left:0;top:990px}
.track text{font-family:"Oswald",Arial,sans-serif;font-weight:500;font-size:12.5px;fill:#fff;text-anchor:middle}
.house-scene{position:absolute;left:0;top:1088px;width:150px;height:72px;background:linear-gradient(180deg,var(--sky),#d8f0f4)}
</style>
</head>
<body>
<main class="journey">
  <div class="top-bar"></div>

  <!-- Stage 1 -->
  <div class="stage-band" style="left:15px;top:76px;width:681px"><span class="stage-no">STAGE 1:</span><span class="stage-name">INITIAL DESIGN PHASE</span></div>

  <svg class="step-icon" style="left:96px;top:110px" viewBox="0 0 70 64" aria-label="Phone icon" role="img">
    <g transform="rotate(-22 35 32)" fill="var(--icon)"><rect x="24" y="4" width="22" height="40" rx="4"/><rect x="27" y="9" width="16" height="28" fill="#fff"/></g>
    <path d="M14 44 q10 -8 22 -2 l18 12 -8 8 -18 -4 z" fill="var(--icon)"/>
  </svg>
  <div class="step-icon icon-placeholder" role="img" aria-label="Two people shaking hands" style="left:322px;top:114px;width:64px;height:60px"></div>
  <svg class="step-icon" style="left:548px;top:112px" viewBox="0 0 70 64" aria-label="Estimate document and calculator icon" role="img">
    <path d="M10 6 h26 l8 8 v44 h-34z" fill="none" stroke="var(--icon)" stroke-width="2.5"/>
    <path d="M6 14 l14 28 -3 5 -3 -3 z" fill="var(--icon)"/>
    <rect x="34" y="22" width="28" height="36" rx="3" fill="var(--icon)"/>
    <rect x="38" y="26" width="20" height="7" fill="#fff"/>
    <g fill="#fff"><rect x="38" y="37" width="5" height="4"/><rect x="45.5" y="37" width="5" height="4"/><rect x="53" y="37" width="5" height="4"/><rect x="38" y="44" width="5" height="4"/><rect x="45.5" y="44" width="5" height="4"/><rect x="53" y="44" width="5" height="4"/><rect x="38" y="51" width="5" height="4"/><rect x="45.5" y="51" width="5" height="4"/><rect x="53" y="51" width="5" height="4"/></g>
  </svg>

  <section class="step-card" style="left:42px;top:190px;height:119px">
    <h3>Initial Contact</h3>
    <p>This is usually by phone or email quick chat with builder - Ben Marlow then an email will be sent with questionaire for you to fill out to see if were a match to work together.</p>
  </section>
  <section class="step-card" style="left:268px;top:190px;height:119px">
    <h3>Initial Face to Face</h3>
    <p>This is were we ??? in depth about your prospect and talk about how we can help you.</p>
  </section>
  <section class="step-card" style="left:493px;top:190px;height:119px">
    <h3>1st Bag Pack Estimate</h3>
    <p>At this stage we will provide you with your 1st initial estimate based on you previous discussions so we can deliver you the best possible product for your budget ( 2-3 days).</p>
  </section>

  <!-- Stage 2 -->
  <div class="stage-band" style="left:15px;top:354px;width:681px"><span class="stage-no">STAGE 2:</span><span class="stage-name">PRELIMINARY PHASE</span></div>

  <div class="step-icon icon-placeholder" role="img" aria-label="Handshake icon" style="left:96px;top:398px;width:72px;height:46px"></div>
  <svg class="step-icon" style="left:322px;top:392px" viewBox="0 0 70 64" aria-label="House icon" role="img">
    <path d="M35 4 L64 30 H56 V60 H14 V30 H6 Z" fill="var(--icon)"/>
    <circle cx="35" cy="22" r="5" fill="#fff"/>
    <rect x="30" y="40" width="10" height="20" fill="#fff"/>
    <rect x="18" y="38" width="8" height="8" fill="#fff"/><rect x="44" y="38" width="8" height="8" fill="#fff"/>
  </svg>
  <svg class="step-icon" style="left:548px;top:392px" viewBox="0 0 70 64" aria-label="Updated estimate icon" role="img">
    <path d="M12 32 a23 23 0 0 1 40 -16" fill="none" stroke="var(--icon)" stroke-width="6"/>
    <path d="M58 32 a23 23 0 0 1 -40 16" fill="none" stroke="var(--icon)" stroke-width="6"/>
    <path d="M46 8 l12 2 -2 12z" fill="var(--icon)"/><path d="M24 56 l-12 -2 2 -12z" fill="var(--icon)"/>
    <rect x="25" y="18" width="20" height="28" rx="2" fill="var(--icon)"/>
    <rect x="28" y="21" width="14" height="5" fill="#fff"/>
    <g fill="#fff"><rect x="28" y="29" width="3.5" height="3"/><rect x="33.2" y="29" width="3.5" height="3"/><rect x="38.5" y="29" width="3.5" height="3"/><rect x="28" y="35" width="3.5" height="3"/><rect x="33.2" y="35" width="3.5" height="3"/><rect x="38.5" y="35" width="3.5" height="3"/></g>
  </svg>

  <section class="step-card" style="left:42px;top:468px;height:174px">
    <h3>1st Preliminary Agreement</h3>
    <p style="margin-top:10px">To ???? forward from ???? both parties needs to sign a preliminary agreement to we can organize the following:</p>
    <p style="margin-top:10px">1. Soil test<br>2. Contour survey<br>3. BAL report ( if requires)<br>(10 days)</p>
  </section>
  <section class="step-card" style="left:268px;top:468px;height:174px">
    <h3>Concept Drawings</h3>
    <p style="margin-top:20px">This is were your plans come together on paper and you get a good feel of what your project will look like. This is the 2nd Prelim Agreement. (5 days)</p>
  </section>
  <section class="step-card" style="left:493px;top:468px;height:174px">
    <h3>Update Estimate</h3>
    <p style="margin-top:20px">This is where we can make any updates to your previous estimate, also submit planning approval if required. (2 days)</p>
  </section>
  <div class="connector right" style="left:224px;top:542px"></div>
  <div class="connector right" style="left:450px;top:542px"></div>

  <svg class="step-icon" style="left:96px;top:670px" viewBox="0 0 70 64" aria-label="Sign contract icon" role="img">
    <path d="M8 4 h26 l8 8 v48 h-34z" fill="none" stroke="var(--icon)" stroke-width="2.5"/>
    <g stroke="var(--icon)" stroke-width="2.5"><line x1="14" y1="22" x2="32" y2="22"/><line x1="14" y1="29" x2="30" y2="29"/><line x1="14" y1="36" x2="26" y2="36"/></g>
    <path d="M62 14 l5 5 -26 26 -7 2 2 -7z" fill="var(--icon)"/>
  </svg>
  <svg class="step-icon" style="left:322px;top:670px" viewBox="0 0 70 64" aria-label="Paint tin icon" role="img">
    <path d="M14 14 q21 -10 42 0 v40 q-21 10 -42 0z" fill="var(--icon)"/>
    <ellipse cx="35" cy="14" rx="21" ry="6" fill="#fff" stroke="var(--icon)" stroke-width="3"/>
    <path d="M22 26 v14 a4 4 0 0 0 8 0 v-10" fill="#fff"/>
  </svg>
  <div class="step-icon icon-placeholder" role="img" aria-label="Rolled floor plan drawing" style="left:555px;top:674px;width:62px;height:58px"></div>

  <div class="variation-note">Any changes past this point is a variation to the quote.</div>
  <div class="variation-line"></div>

  <section class="step-card" style="left:42px;top:745px;height:174px">
    <h3>Sign Contract</h3>
    <p style="margin-top:10px;padding-left:4px">Sign contract, pay deposit from here. We prepare your plans for building permit.</p>
  </section>
  <section class="step-card" style="left:268px;top:745px;height:174px">
    <h3>Colour Selection</h3>
    <p style="margin-top:10px;padding-left:16px">From here we will provide you with a interior designer to help you with your decsions.</p>
  </section>
  <section class="step-card" style="left:493px;top:745px;height:174px">
    <h3>Construction Drawings &amp;<br>??????</h3>
    <p>Here ??? get ?? construction drawings ???? which ??? with the engineer drawings make any amendments to the estimate. This is the 3rd agreement, from here we can also prepare your, ??? and energy assessment ready for building permit (10-15 days)</p>
  </section>
  <div class="connector left" style="left:224px;top:824px"></div>
  <div class="connector left" style="left:450px;top:824px"></div>

  <!-- Stage 3 -->
  <div class="stage-band" style="left:19px;top:947px;width:682px"><span class="stage-no">STAGE 3:</span><span class="stage-name">CONSTRUCTION STAGE</span></div>

  <svg class="track" width="713" height="180" viewBox="0 990 713 180" aria-label="Construction stages track">
    <path d="M540 996 H600 A82 82 0 0 1 600 1160 H535 L523 1124 L535 1088 H612 V1074 H540 Z" fill="var(--green-deep)"/>
    <g stroke="#fff" stroke-width="2">
      <polygon points="55,996 180,996 192,1035 180,1074 55,1074 66,1035" fill="var(--green-mid)"/>
      <polygon points="184,996 308,996 320,1035 308,1074 184,1074 196,1035" fill="var(--green-mid)"/>
      <polygon points="313,996 438,996 450,1035 438,1074 313,1074 325,1035" fill="var(--green-mid)"/>
      <polygon points="443,996 570,996 582,1035 570,1074 443,1074 455,1035" fill="var(--green-mid)"/>
      <polygon points="156,1088 270,1088 260,1124 270,1160 156,1160 144,1124" fill="var(--green-deep)"/>
      <polygon points="275,1088 400,1088 390,1124 400,1160 275,1160 263,1124" fill="var(--green-deep)"/>
      <polygon points="405,1088 530,1088 520,1124 530,1160 405,1160 393,1124" fill="var(--green-deep)"/>
      <polyline points="535,1088 523,1124 535,1160" fill="none"/>
    </g>
    <text x="122" y="1031">PROJECT</text><text x="122" y="1049">SCHEDULING</text>
    <text x="252" y="1031">DONE WHERE BUILDING</text><text x="252" y="1049">DESIGN IN PROGRESS</text>
    <text x="381" y="1040">SLAB DOWN</text>
    <text x="510" y="1040">WALL PLATE</text>
    <text x="207" y="1129">HAND OVER</text>
    <text x="336" y="1129">RIT OUT</text>
    <text x="467" y="1129">LOCK UP</text>
    <text x="596" y="1129">ROOF ON</text>
  </svg>
  <div class="house-scene" role="img" aria-label="Illustration of a finished family home with trees and a white fence"></div>
</main>
</body>
</html>
```